New Business Card Design Project

We want a modern business card that catches the attention of other remodeling companies as well as homeowners. We would like it to be informative but still simple.

Target Market(s)

Residential and other Business's

Contact Information for Business Card

TrellBrix
Phone number is 5153927048
Address is
4817 SW 3rd Lane
Des Moines, Iowa 50313
email is trellbrixco@quamlet.com

Requirements
Must have
• Our tagline
• Honest | Professional | Affordable

```html
<!DOCTYPE html>
<html lang="en">
<head>
<meta charset="utf-8">
<title>TrellBrix Business Card</title>
<link rel="stylesheet" href="https://fonts.googleapis.com/css2?family=Questrial&display=swap">
<style>
  :root {
    --page: #ffffff;
    --card: #413e3f;
    --blue: #3a5fb8;
    --white: #ffffff;
  }
  * { margin: 0; padding: 0; box-sizing: border-box; }
  html, body { width: 1200px; height: 1200px; overflow: hidden; background: var(--page); }
  .canvas { position: relative; width: 1200px; height: 1200px; font-family: 'Questrial', sans-serif; }
  .card {
    position: absolute; left: 220px; width: 760px; height: 456px;
    background: var(--card);
    box-shadow: 8px 10px 14px rgba(0,0,0,0.45);
    color: var(--white);
  }
  .card--front { top: 115px; border-left: 9px solid var(--blue); border-bottom: 8px solid var(--blue); }
  .card--back { top: 631px; border: 1px solid #222; }

  .brand-name, .tagline {
    position: absolute; left: 0; right: 0; text-align: center;
    line-height: 1; white-space: nowrap; font-weight: 400;
  }
  .card--front .brand-name { top: 172px; font-size: 104px; letter-spacing: 2px; }
  .card--front .tagline { top: 278px; font-size: 21px; letter-spacing: 1.5px; }

  .back-brand { position: absolute; left: 56px; top: 192px; width: 318px; height: 80px; color: var(--blue); }
  .card--back .brand-name { top: 0; font-size: 56px; letter-spacing: 1px; }
  .card--back .tagline { top: 58px; font-size: 11px; letter-spacing: 0.8px; }

  .divider { position: absolute; left: 397px; top: 124px; width: 2px; height: 179px; background: var(--white); }

  .contact { position: absolute; left: 449px; top: 174px; list-style: none; font-size: 19px; line-height: 1; }
  .contact li { position: relative; padding-left: 26px; margin-bottom: 11px; }
  .contact li svg { position: absolute; left: 0; top: 1px; width: 17px; height: 17px; fill: var(--blue); }
  .contact .address { line-height: 27px; margin-top: 4px; }
  .contact .address svg { top: 5px; }

  .statement {
    position: absolute; left: 0; right: 0; top: 334px; text-align: center;
    font-size: 19px; line-height: 28.5px;
  }
</style>
</head>
<body>
<main class="canvas">
  <section class="card card--front">
    <div class="brand-name">TRELLBRIX</div>
    <div class="tagline">HONEST | PROFESSIONAL | AFFORDABLE</div>
  </section>

  <section class="card card--back">
    <div class="back-brand">
      <div class="brand-name">TRELLBRIX</div>
      <div class="tagline">HONEST | PROFESSIONAL | AFFORDABLE</div>
    </div>
    <div class="divider"></div>
    <ul class="contact">
      <li><svg viewBox="0 0 24 24"><path d="M6.6 10.8a15.1 15.1 0 0 0 6.6 6.6l2.2-2.2c.3-.3.7-.4 1-.2 1.1.4 2.3.6 3.6.6.6 0 1 .4 1 1V20c0 .6-.4 1-1 1A17 17 0 0 1 3 4c0-.6.4-1 1-1h3.5c.6 0 1 .4 1 1 0 1.3.2 2.5.6 3.6.1.3 0 .7-.2 1z"/></svg>515 392 7048</li>
      <li><svg viewBox="0 0 24 24"><path d="M2 5h20v14H2z M4 7v.3l8 5.4 8-5.4V7zm0 2.7V17h16V9.7l-8 5.4z" fill-rule="evenodd"/></svg>trellbrixco@quamlet.com</li>
      <li class="address"><svg viewBox="0 0 24 24"><path d="M12 2a7 7 0 0 0-7 7c0 5.3 7 13 7 13s7-7.7 7-13a7 7 0 0 0-7-7zm0 9.5A2.5 2.5 0 1 1 12 6.5a2.5 2.5 0 0 1 0 5z"/></svg>4817 SW 3rd Lane<br>Marlowe Springs,Iowa 50417</li>
    </ul>
    <p class="statement">At TrellBrix we feel<br>honesty,professionalism and affordability<br>are the backbone of a positive Customer experience</p>
  </section>
</main>
</body>
</html>
```